Business Card for Professional Photographer

I'm looking for an eye catching modern clean design that compliments my logo/ website fonts & colours.
I specialise in architecture, corporate & commercial photography so I'm marketing to professional clients rather than portrait / wedding clients.

I would prefer to not have a solid black design.

My logo brand guide is as follows :

Main front font. : Reislust
Main font colour : #fff
Slogan front font : Ubuntu Bold
Monogram front font : Venti Medium
Container colour : #fff

I need print ready files in pdf .png & .eps formats.

Included in the files below are some screen grabs as reference to font & colours etc.

```html
<!DOCTYPE html>
<html lang="en">
<head>
<meta charset="utf-8">
<title>Clearline Studio – Business Card</title>
<link href="https://fonts.googleapis.com/css2?family=Questrial&family=Montserrat:wght@700&display=swap" rel="stylesheet">
<style>
  :root {
    --backdrop: #3a3431;
    --card: #ffffff;
    --gold: #c9a24a;
    --gold-light: #dcc073;
    --ink: #4a4a4a;
    --ink-soft: #6b6b6b;
  }
  * { box-sizing: border-box; margin: 0; padding: 0; }
  html, body {
    width: 1200px;
    height: 716px;
    overflow: hidden;
    background: var(--backdrop);
  }
  .canvas {
    width: 1200px;
    height: 716px;
    display: flex;
    align-items: center;
    justify-content: center;
    gap: 60px;
  }
  .card {
    width: 530px;
    height: 303px;
    background: var(--card);
    position: relative;
    box-shadow: 0 10px 30px rgba(0,0,0,0.35);
  }
  /* Brand lockup */
  .brand {
    display: flex;
    align-items: center;
    gap: 14px;
    font-family: "Questrial", sans-serif;
    color: var(--gold);
  }
  .brand-dot {
    width: 46px;
    height: 46px;
    border: 3px solid var(--gold);
    border-radius: 50%;
    flex: none;
  }
  .brand-text { display: flex; flex-direction: column; }
  .brand-name {
    font-size: 24px;
    letter-spacing: 4px;
    text-transform: uppercase;
    line-height: 1.1;
  }
  .brand-tagline {
    font-size: 8px;
    letter-spacing: 3px;
    margin-top: 4px;
  }
  /* Front */
  .card-front .brand {
    position: absolute;
    left: 50%;
    top: 50%;
    transform: translate(-50%, -50%);
  }
  /* Back */
  .card-back .brand {
    position: absolute;
    right: 30px;
    top: 40px;
  }
  .card-back .brand-dot { width: 34px; height: 34px; border-width: 2px; }
  .card-back .brand-name { font-size: 17px; letter-spacing: 3px; }
  .card-back .brand-tagline { font-size: 6px; letter-spacing: 2.4px; }
  .contact {
    position: absolute;
    left: 34px;
    bottom: 44px;
    font-family: "Questrial", sans-serif;
    color: var(--ink);
  }
  .contact-name {
    font-family: "Montserrat", sans-serif;
    font-weight: 700;
    font-size: 19px;
    color: var(--gold);
  }
  .contact-role {
    font-size: 12px;
    color: var(--ink-soft);
    margin: 2px 0 10px;
  }
  .contact-line {
    font-size: 13px;
    line-height: 1.55;
  }
  .contact-label {
    color: var(--gold);
    font-weight: 700;
    margin-right: 4px;
  }
  .contact-accent { color: var(--gold); }
</style>
</head>
<body>
  <main class="canvas">
    <section class="card card-front" aria-label="Card front">
      <div class="brand">
        <span class="brand-dot"></span>
        <div class="brand-text">
          <span class="brand-name">Clearline Studio</span>
          <span class="brand-tagline">Architecture Corporate Commercial</span>
        </div>
      </div>
    </section>

    <section class="card card-back" aria-label="Card back">
      <div class="brand">
        <span class="brand-dot"></span>
        <div class="brand-text">
          <span class="brand-name">Clearline Studio</span>
          <span class="brand-tagline">Architecture Corporate Commercial</span>
        </div>
      </div>
      <div class="contact">
        <p class="contact-name">Dana Whitfield</p>
        <p class="contact-role">Development Manager</p>
        <p class="contact-line"><span class="contact-label">P</span>: 0400 123 987</p>
        <p class="contact-line"><span class="contact-label">M</span>: dana@clearlinestudio.com.au</p>
        <p class="contact-line"><span class="contact-label">W</span>: www.<span class="contact-accent">clearlinestudio</span>.com.au</p>
      </div>
    </section>
  </main>
</body>
</html>
```